KB Rubbish Removal Business Card

Hey,
I need a double sided business card designed for a rubbish removal business based in Australia. Logo is already chosen, similar colours preferred for both sides of the business card.

Details to include:

Front:

KB Rubbish Removal
Darren Holloway
Managing Director
Mobile: 0471 902 146
Email: darren@kbrubbishremoval.com.au
Website: kbrubbishremoval.com.au

Rear:

How did we do?
kbrubbishremoval.com.au/review

```html
<!DOCTYPE html>
<html lang="en">
<head>
<meta charset="utf-8">
<title>KB Rubbish Removal Business Card</title>
<link rel="stylesheet" href="https://fonts.googleapis.com/css2?family=Raleway:wght@600;700&family=Roboto:wght@300;400&display=swap">
<style>
  :root {
    --stage: #2b2b2d;
    --card-white: #ffffff;
    --card-black: #1c1c1e;
    --card-black-soft: #2a2a2d;
    --brand-green: #15803f;
    --brand-green-light: #5cc45f;
    --ink-dark: #3a3a3c;
    --ink-grey: #6b6b6e;
    --band-dark: #333335;
  }
  * { box-sizing: border-box; margin: 0; padding: 0; }
  html, body { width: 1200px; height: 929px; overflow: hidden; }
  body { background: var(--stage); position: relative; }

  .card {
    position: absolute;
    width: 560px;
    height: 320px;
    border-radius: 3px;
    box-shadow: 0 18px 40px rgba(0,0,0,.45);
    overflow: hidden;
  }

  .brand-dot { width: 30px; height: 30px; border-radius: 50%; flex: none; }
  .brand-name {
    font-family: "Raleway", sans-serif;
    font-weight: 600;
    font-size: 18px;
    letter-spacing: 0;
  }

  /* Rear side */
  .card--rear {
    left: 110px; top: 100px;
    background: radial-gradient(ellipse at 50% 30%, var(--card-black-soft), var(--card-black) 75%);
    color: #fff;
    display: flex; flex-direction: column; align-items: center; justify-content: center;
    text-align: center;
  }
  .rear-brand { display: flex; align-items: center; gap: 10px; margin-bottom: 34px; }
  .rear-brand .brand-dot { background: var(--brand-green-light); }
  .rear-brand .brand-name { color: #ffffff; }
  .rear-question, .rear-url {
    font-family: "Raleway", sans-serif; font-weight: 700; text-transform: uppercase;
    letter-spacing: .3px; line-height: 1.35;
  }
  .rear-question { font-size: 17px; }
  .rear-url { font-size: 19px; }

  /* Front side */
  .card--front { left: 530px; top: 500px; background: var(--card-white); }
  .front-brand {
    position: absolute; right: 48px; top: 58px;
    display: flex; align-items: center; gap: 10px;
  }
  .front-brand .brand-dot { background: var(--brand-green); }
  .front-brand .brand-name { color: var(--ink-dark); }
  .contact-block { position: absolute; left: 40px; top: 150px; }
  .person-name {
    font-family: "Raleway", sans-serif; font-weight: 700; font-size: 21px;
    color: var(--brand-green); text-transform: uppercase; letter-spacing: .3px;
  }
  .person-role {
    font-family: "Raleway", sans-serif; font-weight: 700; font-size: 15px;
    color: var(--ink-dark); margin-top: 2px; margin-bottom: 10px;
  }
  .contact-list { list-style: none; }
  .contact-list li {
    display: flex; align-items: center; gap: 9px;
    font-family: "Roboto", sans-serif; font-weight: 300; font-size: 15px;
    color: var(--ink-grey); line-height: 21px;
  }
  .contact-icon { width: 15px; height: 15px; flex: none; }
  .front-band { position: absolute; left: 0; bottom: 0; width: 560px; height: 70px; }
</style>
</head>
<body>

<section class="card card--rear" aria-label="Business card rear">
  <div class="rear-brand">
    <span class="brand-dot"></span>
    <span class="brand-name">KB Rubbish Removal</span>
  </div>
  <p class="rear-question">How did we do?</p>
  <p class="rear-url">kbrubbishremoval.com.au/review</p>
</section>

<section class="card card--front" aria-label="Business card front">
  <div class="front-brand">
    <span class="brand-dot"></span>
    <span class="brand-name">KB Rubbish Removal</span>
  </div>

  <div class="contact-block">
    <h1 class="person-name">Darren Holloway</h1>
    <p class="person-role">Managing Director</p>
    <ul class="contact-list">
      <li>
        <svg class="contact-icon" viewBox="0 0 24 24"><path fill="var(--brand-green)" d="M6.6 10.8a15.1 15.1 0 0 0 6.6 6.6l2.2-2.2a1 1 0 0 1 1-.25 11.4 11.4 0 0 0 3.6.57 1 1 0 0 1 1 1V20a1 1 0 0 1-1 1A17 17 0 0 1 3 4a1 1 0 0 1 1-1h3.5a1 1 0 0 1 1 1c0 1.25.2 2.45.57 3.57a1 1 0 0 1-.25 1z"/></svg>
        0471 902 146
      </li>
      <li>
        <svg class="contact-icon" viewBox="0 0 24 24"><rect x="2" y="5" width="20" height="14" fill="var(--brand-green)"/><path d="M2.5 5.5 12 13l9.5-7.5M2.5 18.5l7-6.5M21.5 18.5l-7-6.5" fill="none" stroke="#fff" stroke-width="1.4"/></svg>
        darren@kbrubbishremoval.com.au
      </li>
      <li>
        <svg class="contact-icon" viewBox="0 0 24 24"><g fill="none" stroke="var(--brand-green)" stroke-width="2"><circle cx="12" cy="12" r="9"/><path d="M3 12h18M12 3c3 3 3 15 0 18M12 3c-3 3-3 15 0 18"/></g></svg>
        kbrubbishremoval.com.au
      </li>
    </ul>
  </div>

  <svg class="front-band" viewBox="0 0 560 70" preserveAspectRatio="none" aria-hidden="true">
    <polygon points="0,50 400,50 400,70 0,70" fill="var(--brand-green)"/>
    <polygon points="402,70 410,24 560,24 560,70" fill="var(--band-dark)"/>
  </svg>
</section>

</body>
</html>
```